Single Page Timetracking Dashboard Desktop App UI Design (Figma Link required)

Main Idea: a SaaS tool where employees can add their time and project in a playful way. There is a infographics and a list with tasks as well.

Based on the attached concept.png the brief is following:

- check the attached rough scribble
- add own ideas or change things if they add value
- Style: colourful, nerdy, professional saas, modern, beautiful, white space
- Quality expectation: inspiration1+2.png
- I will need a Figma link
- desktop only
- make something fresh and unique

Process:
I need to include 2-3 feedback rounds that will span probably around 7 days

Target Market(s)

Internal Business Tool for a Software Development Company

Industry/Entity Type

IT

Other font styles liked:
• Could be monospace, not a must though

Requirements
Must have
• At least one page; Figma Link to the design;
Nice to have
• Microinterations like drop-down, hover/active colors; functionality specifications
Should not have
• Mobile view

```html
<!DOCTYPE html>
<html lang="en">
<head>
<meta charset="utf-8">
<title>Time Tracking Dashboard</title>
<link rel="stylesheet" href="https://fonts.googleapis.com/css2?family=Roboto:wght@400;500;700&display=swap">
<style>
:root{
  --backdrop:#cfcfcf;
  --white:#ffffff;
  --canvas:#f8f7fc;
  --panel:#f1eff6;
  --ink:#1f1f24;
  --muted:#6e6e78;
  --soft:#8d8d96;
  --pink:#f24f86;
  --pink-soft:#fde6ee;
  --cyan:#17b8d6;
  --cyan-soft:#e8f8fb;
  --yellow:#f7bd16;
  --blue:#1f3fa3;
  --green:#2cb11c;
  --red:#ee1515;
  --shadow:0 2px 8px rgba(40,30,80,.06);
}
*{box-sizing:border-box;margin:0;padding:0}
html,body{width:1200px;height:2552px;overflow:hidden}
body{background:var(--backdrop);font-family:"Roboto",sans-serif;color:var(--ink);position:relative}
.app{position:absolute;left:99px;top:83px;width:1001px;height:2380px;background:var(--white);border-radius:30px;overflow:hidden}
.main-bg{position:absolute;left:156px;top:66px;right:0;bottom:0;background:var(--canvas);border-top-left-radius:22px}

/* brand & header */
.brand{position:absolute;left:38px;top:36px;display:flex;align-items:center;gap:6px;font-size:15px;font-weight:500;color:var(--pink)}
.brand-dot{width:14px;height:14px;border-radius:50%;background:var(--pink)}
.welcome{position:absolute;left:163px;top:16px}
.welcome small{display:block;font-size:10px;color:var(--muted)}
.welcome strong{display:block;font-size:16px;font-weight:500;margin-top:4px}
.mascot{position:absolute;left:290px;top:18px;width:36px;height:36px;border-radius:50%;background:radial-gradient(circle,#ffd54a,#f5a623)}
.header-icon{position:absolute;top:26px}
.avatar{position:absolute;left:895px;top:14px;width:42px;height:42px;border-radius:50%;border:2px solid #e8e8ee;background:linear-gradient(160deg,#dfe6ef,#9bb0c6)}
.avatar-badge{position:absolute;left:928px;top:41px;width:14px;height:14px;border-radius:50%;background:var(--green);border:2px solid var(--white)}

/* sidebar */
.nav-item{position:absolute;left:0;width:156px;height:35px;display:flex;align-items:center;padding-left:37px;gap:16px;font-size:10px}
.nav-item.active{background:var(--cyan-soft);border-right:3px solid var(--cyan)}
.nav-item svg{width:11px;height:11px}
.logout{position:absolute;left:34px;top:2325px;display:flex;align-items:center;gap:12px;font-size:12px;font-weight:500}

/* section titles */
.section-title{position:absolute;left:183px;font-size:16px;font-weight:500;text-transform:uppercase}
.dropdown{position:absolute;left:850px;width:121px;height:27px;background:var(--cyan-soft);color:var(--cyan);font-size:13px;display:flex;align-items:center;justify-content:space-between;padding:0 14px 0 20px}
.see-all{position:absolute;left:579px;font-size:9px;font-weight:500;text-decoration:underline;letter-spacing:.2px}

/* calendar */
.calendar{position:absolute;left:181px;top:123px;width:244px;height:218px;background:var(--white);border-radius:16px;box-shadow:var(--shadow)}
.cal-arrow{position:absolute;top:17px;width:22px;height:22px;border-radius:50%;background:#eeeef4;display:flex;align-items:center;justify-content:center}
.cal-month{position:absolute;left:0;right:0;top:20px;text-align:center;font-size:13px;font-weight:500}
.day{position:absolute;width:18px;height:18px;margin-left:-9px;margin-top:-9px;border-radius:50%;font-size:7.5px;display:flex;align-items:center;justify-content:center;color:#333}
.day.today{background:var(--yellow);color:var(--white)}
.day.marked{background:var(--pink);color:var(--white)}
.day.picked{background:var(--cyan);color:var(--white)}

/* selectors */
.select-btn{position:absolute;left:438px;width:157px;height:42px;border-radius:10px;color:var(--white);font-size:10px;font-weight:500;display:flex;align-items:center;justify-content:space-between;padding:0 9px 0 16px}
.select-btn i{width:22px;height:22px;border-radius:50%;background:rgba(255,255,255,.35);display:flex;align-items:center;justify-content:center}
.project-pink{background:var(--pink);top:125px}
.type-cyan{background:var(--cyan);top:178px}
.option{position:absolute;left:441px;font-size:8.5px;color:var(--muted)}
.slot{position:absolute;width:82px;height:50px;background:var(--white);box-shadow:var(--shadow);font-size:10px;font-weight:500;display:flex;align-items:center;justify-content:center}
.slot.on{background:var(--pink-soft);border:1px solid #f49ab8}
.note{position:absolute;left:183px;top:377px;width:409px;height:84px;background:var(--white);box-shadow:var(--shadow);padding:16px 16px;font-size:9.5px;color:#444}
.total-time{position:absolute;right:134px;top:406px;font-size:26px;font-weight:500}
.save{position:absolute;left:888px;top:400px;width:81px;height:39px;background:var(--pink);color:var(--white);font-size:12px;font-weight:700;display:flex;align-items:center;justify-content:center}

/* statistics */
.stats-panel{position:absolute;left:187px;top:552px;width:785px;height:263px;background:var(--panel);border-radius:16px}
.stat-card{position:absolute;top:16px;width:355px;height:230px;background:var(--white)}
.stat-card h3{position:absolute;left:20px;top:21px;font-size:12px;font-weight:500}
.total-pill{position:absolute;top:14px;right:15px;width:121px;height:27px;background:var(--pink-soft);color:var(--pink);font-size:12px;display:flex;align-items:center;justify-content:center}
.legend{position:absolute;right:18px;font-size:7.5px;color:#333;text-align:right}
.donut{position:absolute;left:14px;top:52px}

/* tasks */
.day-label{position:absolute;left:193px;font-size:15px;font-weight:500;color:var(--cyan)}
.day-hours{position:absolute;right:35px;font-size:12px}
.task{position:absolute;left:186px;width:780px;height:163px;background:var(--white);box-shadow:var(--shadow)}
.task-bar{position:absolute;left:18px;top:15px;width:743px;height:38px;border-radius:20px;background:var(--cyan-soft);font-size:13px;display:flex;align-items:center;padding-left:18px}
.task-bar .act{position:absolute;top:0;height:38px;width:52px;display:flex;align-items:center;justify-content:center;color:var(--white);font-size:12.5px}
.act.delete{left:602px;background:var(--cyan)}
.act.edit{left:660px;background:var(--pink)}
.task-title{position:absolute;left:27px;top:78px;font-size:24px;font-weight:700}
.task-hours{position:absolute;right:18px;top:78px;font-size:24px;font-weight:500}
.task-desc{position:absolute;left:27px;top:122px;font-size:15.5px;color:var(--muted)}
.task-date{position:absolute;right:18px;top:122px;font-size:15.5px;color:var(--muted)}
</style>
</head>
<body>
<div class="app">
  <div class="main-bg"></div>

  <div class="brand"><span class="brand-dot"></span>Hourloop</div>
  <div class="welcome"><small>Welcome Back,</small><strong>Saas Application</strong></div>
  <div class="mascot" role="img" aria-label="Waving cartoon mascot"></div>
  <svg class="header-icon" style="left:816px" width="18" height="18" viewBox="0 0 18 18" fill="none" stroke="#888" stroke-width="1.4"><circle cx="8" cy="8" r="6"/><path d="M12.5 12.5 16 16"/></svg>
  <svg class="header-icon" style="left:857px" width="18" height="18" viewBox="0 0 18 18" fill="none" stroke="#888" stroke-width="1.3"><path d="M4 13V8a5 5 0 0 1 10 0v5l1.5 1.5h-13z"/><path d="M7.5 16a1.6 1.6 0 0 0 3 0"/><circle cx="13.5" cy="3.5" r="2" fill="#f24f86" stroke="none"/></svg>
  <div class="avatar" role="img" aria-label="User profile photo"></div>
  <div class="avatar-badge"></div>

  <div class="nav-item active" style="top:104px"><svg viewBox="0 0 12 12" fill="none" stroke="#17b8d6" stroke-width="1.3"><circle cx="6" cy="6" r="5"/><path d="M6 3v3h2"/></svg>Clock</div>
  <div class="nav-item" style="top:156px"><svg viewBox="0 0 12 12" fill="#17b8d6"><rect x="1" y="6" width="1.6" height="5"/><rect x="4" y="3" width="1.6" height="8"/><rect x="7" y="5" width="1.6" height="6"/><rect x="10" y="2" width="1.6" height="9"/></svg>Statistics</div>
  <div class="nav-item" style="top:208px"><svg viewBox="0 0 12 12" fill="#17b8d6"><rect x="1" y="2" width="10" height="2"/><rect x="1" y="5" width="10" height="2"/><rect x="1" y="8" width="10" height="2"/></svg>Task</div>
  <div class="nav-item" style="top:261px"><svg viewBox="0 0 12 12" fill="#17b8d6"><circle cx="6" cy="3.5" r="2.5"/><path d="M1.5 11a4.5 4 0 0 1 9 0z"/></svg>User</div>
  <div class="logout"><svg width="10" height="12" viewBox="0 0 10 12" fill="#17b8d6"><rect x="0" y="5" width="10" height="7" rx="1"/><path d="M2.5 5V3.5a2.5 2.5 0 0 1 5 0V5" fill="none" stroke="#17b8d6" stroke-width="1.4"/></svg>Logout</div>

  <!-- Track your time -->
  <div class="section-title" style="top:88px">Track your time</div>
  <div class="calendar">
    <div class="cal-arrow" style="left:20px"><svg width="8" height="8" viewBox="0 0 8 8" fill="none" stroke="#333" stroke-width="1.2"><path d="M5 1 2 4l3 3"/></svg></div>
    <div class="cal-month">October 2023</div>
    <div class="cal-arrow" style="left:202px"><svg width="8" height="8" viewBox="0 0 8 8" fill="none" stroke="#333" stroke-width="1.2"><path d="M3 1l3 3-3 3"/></svg></div>
    <div class="day" style="left:29px;top:69px">1</div><div class="day" style="left:60px;top:69px">2</div><div class="day" style="left:92px;top:69px">3</div><div class="day" style="left:123px;top:69px">4</div><div class="day" style="left:154px;top:69px">5</div><div class="day" style="left:186px;top:69px">6</div><div class="day" style="left:217px;top:69px">7</div>
    <div class="day" style="left:29px;top:100px">8</div><div class="day" style="left:60px;top:100px">9</div><div class="day today" style="left:92px;top:100px">10</div><div class="day" style="left:123px;top:100px">11</div><div class="day" style="left:154px;top:100px">12</div><div class="day" style="left:186px;top:100px">13</div><div class="day" style="left:217px;top:100px">14</div>
    <div class="day" style="left:29px;top:132px">15</div><div class="day" style="left:60px;top:132px">16</div><div class="day" style="left:92px;top:132px">17</div><div class="day" style="left:123px;top:132px">18</div><div class="day" style="left:154px;top:132px">19</div><div class="day" style="left:186px;top:132px">20</div><div class="day" style="left:217px;top:132px">21</div>
    <div class="day" style="left:29px;top:163px">22</div><div class="day" style="left:60px;top:163px">23</div><div class="day marked" style="left:92px;top:163px">24</div><div class="day" style="left:123px;top:163px">25</div><div class="day" style="left:154px;top:163px">26</div><div class="day" style="left:186px;top:163px">27</div><div class="day" style="left:217px;top:163px">28</div>
    <div class="day picked" style="left:29px;top:194px">29</div><div class="day" style="left:60px;top:194px">30</div><div class="day" style="left:92px;top:194px">31</div>
  </div>

  <div class="select-btn project-pink">Select Project<i><svg width="8" height="6" viewBox="0 0 8 6" fill="none" stroke="#fff" stroke-width="1.3"><path d="M1 1.5 4 4.5 7 1.5"/></svg></i></div>
  <div class="select-btn type-cyan">Select Type<i><svg width="8" height="6" viewBox="0 0 8 6" fill="none" stroke="#fff" stroke-width="1.3"><path d="M1 1.5 4 4.5 7 1.5"/></svg></i></div>
  <div class="option" style="top:233px">Customer 1 - Project 1</div>
  <div class="option" style="top:259px">Customer 2 - Project 2</div>
  <div class="option" style="top:286px">Customer 1 - Project 2</div>
  <div class="option" style="top:311px">Customer with long Name and Project</div>

  <div class="slot on" style="left:614px;top:125px">1h</div>
  <div class="slot" style="left:707px;top:125px">2h</div>
  <div class="slot" style="left:799px;top:125px">3h</div>
  <div class="slot" style="left:890px;top:125px">4h</div>
  <div class="slot" style="left:614px;top:193px">5h</div>
  <div class="slot" style="left:707px;top:193px">6h</div>
  <div class="slot" style="left:799px;top:193px">7h</div>
  <div class="slot" style="left:890px;top:193px">8h</div>
  <div class="slot" style="left:614px;top:282px">0m</div>
  <div class="slot on" style="left:707px;top:282px">15m</div>
  <div class="slot" style="left:799px;top:282px">30m</div>
  <div class="slot" style="left:890px;top:282px">45m</div>

  <div class="note">What did you do?</div>
  <div class="total-time">1h 15m</div>
  <div class="save">SAVE</div>

  <!-- Statistics -->
  <div class="section-title" style="top:516px">Statistics</div>
  <div class="dropdown" style="top:512px">Monate<svg width="8" height="6" viewBox="0 0 8 6" fill="none" stroke="#17b8d6" stroke-width="1.2"><path d="M1 1.5 4 4.5 7 1.5"/></svg></div>
  <div class="stats-panel">
    <div class="stat-card" style="left:21px">
      <h3>Current Month</h3>
      <div class="total-pill">Total - 50:45 h</div>
      <svg class="donut" width="164" height="164" viewBox="0 0 164 164" fill="none" stroke-width="26" stroke-linecap="round">
        <g transform="rotate(-90 82 82)">
          <circle cx="82" cy="82" r="66" stroke="var(--pink)" stroke-dasharray="38 377" stroke-dashoffset="-4"/>
          <circle cx="82" cy="82" r="66" stroke="var(--cyan)" stroke-dasharray="350 65" stroke-dashoffset="-62"/>
        </g>
        <circle cx="82" cy="16.5" r="4.5" fill="#fff" stroke="none"/>
        <circle cx="133" cy="40" r="4.5" fill="#fff" stroke="none"/>
      </svg>
      <div class="legend" style="top:181px">40:45 h Customer A (89%)</div>
      <div class="legend" style="top:202px">10:00 h Customer B (11%)</div>
    </div>
    <div class="stat-card" style="left:408px">
      <h3>September</h3>
      <div class="total-pill">Gesamt - 114:00h</div>
      <svg class="donut" width="164" height="164" viewBox="0 0 164 164" fill="none" stroke-width="26" stroke-linecap="round">
        <g transform="rotate(-90 82 82)">
          <circle cx="82" cy="82" r="66" stroke="var(--pink)" stroke-dasharray="48 367" stroke-dashoffset="-6"/>
          <circle cx="82" cy="82" r="66" stroke="var(--yellow)" stroke-dasharray="50 365" stroke-dashoffset="-80"/>
          <circle cx="82" cy="82" r="66" stroke="var(--blue)" stroke-dasharray="55 360" stroke-dashoffset="-155"/>
          <circle cx="82" cy="82" r="66" stroke="var(--green)" stroke-dasharray="48 367" stroke-dashoffset="-236"/>
          <circle cx="82" cy="82" r="66" stroke="var(--red)" stroke-dasharray="38 377" stroke-dashoffset="-308"/>
          <circle cx="82" cy="82" r="66" stroke="var(--cyan)" stroke-dasharray="35 380" stroke-dashoffset="-372"/>
        </g>
        <circle cx="82" cy="16.5" r="4.5" fill="#fff" stroke="none"/>
        <circle cx="134" cy="41" r="4.5" fill="#fff" stroke="none"/>
        <circle cx="144" cy="111" r="4.5" fill="#fff" stroke="none"/>
        <circle cx="105" cy="143" r="4.5" fill="#fff" stroke="none"/>
        <circle cx="45" cy="137" r="4.5" fill="#fff" stroke="none"/>
        <circle cx="16" cy="86" r="4.5" fill="#fff" stroke="none"/>
      </svg>
      <div class="legend" style="top:70px">40:45 h Customer A (53%)</div>
      <div class="legend" style="top:96px">8:15 h Customer B (13%)</div>
      <div class="legend" style="top:122px">20:00 h Customer C (34%)</div>
      <div class="legend" style="top:149px">22:45 h Customer D (53%)</div>
      <div class="legend" style="top:175px">02:15 h Customer E (13%)</div>
      <div class="legend" style="top:201px">20:00 h Customer F (34%)</div>
    </div>
  </div>
  <div class="see-all" style="top:836px">SEE ALL</div>

  <!-- Tasks -->
  <div class="section-title" style="top:918px">Your tasks</div>
  <div class="dropdown" style="top:913px">Filter<svg width="8" height="6" viewBox="0 0 8 6" fill="none" stroke="#17b8d6" stroke-width="1.2"><path d="M1 1.5 4 4.5 7 1.5"/></svg></div>

  <div class="day-label" style="top:965px">WEDNESDAY</div>
  <div class="day-hours" style="top:968px">7H 30M</div>
  <div class="task" style="top:998px">
    <div class="task-bar">Coding<span class="act delete">Delete</span><span class="act edit">Edit</span></div>
    <div class="task-title">Customer A Project 1</div><div class="task-hours">4h 30m</div>
    <div class="task-desc">Some Description what the user did on that project</div><div class="task-date">December 9th</div>
  </div>

  <div class="day-label" style="top:1211px">TUESDAY</div>
  <div class="day-hours" style="top:1214px">7H 30M</div>
  <div class="task" style="top:1244px">
    <div class="task-bar">Project Management<span class="act delete">Delete</span><span class="act edit">Edit</span></div>
    <div class="task-title">Customer B Project 1</div><div class="task-hours">3h</div>
    <div class="task-desc">Some Description what the user did on that project</div><div class="task-date">December 9th</div>
  </div>
  <div class="task" style="top:1447px">
    <div class="task-bar">Project Management<span class="act delete">Delete</span><span class="act edit">Edit</span></div>
    <div class="task-title">Customer A Project 1</div><div class="task-hours">5h</div>
    <div class="task-desc">Some Description what the user did on that project</div><div class="task-date">December 9th</div>
  </div>
  <div class="task" style="top:1651px">
    <div class="task-bar">Coding<span class="act delete">Delete</span><span class="act edit">Edit</span></div>
    <div class="task-title">Customer A Project 1</div><div class="task-hours">4h 30m</div>
    <div class="task-desc">Some Description what the user did on that project</div><div class="task-date">December 9th</div>
  </div>

  <div class="day-label" style="top:1864px">MONDAY</div>
  <div class="day-hours" style="top:1867px">7H 30M</div>
  <div class="task" style="top:1897px">
    <div class="task-bar">Meeting<span class="act delete">Delete</span><span class="act edit">Edit</span></div>
    <div class="task-title">Customer B Project 1</div><div class="task-hours">2h 30m</div>
    <div class="task-desc">Some Description what the user did on that project</div><div class="task-date">December 9th</div>
  </div>
  <div class="task" style="top:2101px">
    <div class="task-bar">Meeting<span class="act delete">Delete</span><span class="act edit">Edit</span></div>
    <div class="task-title">Customer A Project 1</div><div class="task-hours">15m</div>
    <div class="task-desc">Some Description what the user did on that project</div><div class="task-date">December 9th</div>
  </div>
  <div class="see-all" style="top:2291px">SEE ALL</div>
</div>
</body>
</html>
```